Doors for Chiropractic Office

In my chiropractic office I have 6 treatment rooms and 2 massage rooms. The entire office is going through a remodel. The overall color scheme is very earth tones but in order to add some color, the 6 doors to the treatment rooms will all be a separate color (Red, Blue, Yellow, Green etc)
I need to number each room 1,2,3,4,5,6 and the 2 massage rooms. I had the idea of putting a giant number on each door, so I am looking for some graphic ideas for that project.
The rooms are located with 4 on each side of a long hallway with the 2 massage rooms at the end.
The purpose of numbering each door is to direct the patients where to go.
I have uploaded pictures of the hall way. Pardon the dust since we are under construction but hopefully it gives you an idea of the layout. The door colors will change as stated above.

Requirements
Nice to have
• I would like to see someone come up with a design where each number for the doors are created out of vertebrae's.

```html
<!DOCTYPE html>
<html lang="en">
<head>
<meta charset="utf-8">
<title>Door Signs – Room Name / Number</title>
<link rel="stylesheet" href="https://fonts.googleapis.com/css2?family=Bebas+Neue&family=Oswald:wght@500;600&display=swap">
<style>
  :root {
    --brand-blue: #3aaee0;
    --massage-blue: #27aae1;
    --board-grey: #b3b3b3;
    --panel-grey: #6d6d72;
    --cream: #f4f0e3;
    --frame-cream: #fcf8ea;
    --ink: #1e1e1e;
    --room-1: #ee7a1f;
    --room-2: #a3206f;
    --room-3: #4e3f8c;
    --room-4: #2d88b2;
    --room-5: #78a332;
    --room-6: #2e8c62;
  }
  * { margin: 0; padding: 0; box-sizing: border-box; }
  html, body { width: 1200px; height: 1200px; overflow: hidden; background: #fff; }
  .board { width: 1200px; height: 1200px; display: block; }
  .number { font-family: "Bebas Neue", sans-serif; }
  .label { font-family: "Oswald", sans-serif; font-weight: 600; fill: var(--ink); }
  .brand { font-family: "Oswald", sans-serif; font-weight: 500; fill: var(--brand-blue); }
  .title { font-family: "Bebas Neue", sans-serif; fill: var(--brand-blue); }
  .massage-label { font-family: "Oswald", sans-serif; font-weight: 600; fill: #fff; }
</style>
</head>
<body>
<svg class="board" viewBox="0 0 1100 1100" xmlns="http://www.w3.org/2000/svg">
  <defs>
    <linearGradient id="door-fill" x1="0" y1="0" x2="0" y2="1">
      <stop offset="0" stop-color="#8a6b60"/>
      <stop offset="0.45" stop-color="#a67b6b"/>
      <stop offset="1" stop-color="#8a6b60"/>
    </linearGradient>
    <linearGradient id="header-shadow" x1="0" y1="0" x2="0" y2="1">
      <stop offset="0" stop-color="#8a8a8a"/>
      <stop offset="1" stop-color="#b3b3b3" stop-opacity="0"/>
    </linearGradient>

    <g id="treatment-plate">
      <rect x="0" y="13" width="10" height="118"/>
      <rect x="0" y="123" width="262" height="8"/>
      <path d="M10,0 L80,0 Q215,4 273,70 L273,123 L10,123 Z" fill="var(--cream)"/>
      <circle cx="91" cy="76" r="4" fill="var(--brand-blue)"/>
      <text class="brand" x="98" y="79" font-size="8">RIDGEWAY SPINE</text>
      <text class="label" x="85" y="108" font-size="22">TREATMENT ROOM</text>
    </g>

    <g id="massage-plate">
      <rect x="-10" y="13" width="10" height="120" fill="#fff"/>
      <rect x="-10" y="123" width="262" height="10" fill="#fff"/>
      <path d="M0,0 L80,0 Q210,4 263,70 L263,123 L0,123 Z" fill="var(--massage-blue)"/>
      <circle cx="38" cy="43" r="27" fill="#fff"/>
      <circle cx="93" cy="40" r="4" fill="#fff"/>
      <text class="brand" x="100" y="43" font-size="8" style="fill:#fff">RIDGEWAY SPINE</text>
      <text class="massage-label" x="10" y="112" font-size="40">MASSAGE ROOM</text>
    </g>
  </defs>

  <!-- header -->
  <rect class="header" x="0" y="0" width="1100" height="125" fill="#fff"/>
  <circle cx="118" cy="60" r="14" fill="var(--brand-blue)"/>
  <text class="brand" x="140" y="72" font-size="30">RIDGEWAY SPINE</text>
  <text class="title" x="390" y="88" font-size="74" letter-spacing="1">DOOR - ROOM NAME/NUMBER</text>

  <!-- board -->
  <rect x="0" y="125" width="1100" height="950" fill="var(--board-grey)"/>
  <rect x="0" y="125" width="1100" height="22" fill="url(#header-shadow)"/>

  <!-- door -->
  <g class="door">
    <rect x="85" y="187" width="303" height="828" fill="var(--frame-cream)"/>
    <rect x="102" y="205" width="270" height="810" fill="url(#door-fill)"/>
    <circle cx="340" cy="668" r="12" fill="#f5f1e6"/>
    <g transform="translate(150 377) scale(0.64)" fill="var(--room-1)">
      <use href="#treatment-plate"/>
      <text class="number" x="28" y="108" font-size="112" fill="var(--room-1)">1</text>
    </g>
  </g>

  <!-- treatment room plates -->
  <g transform="translate(445 245)" fill="var(--room-1)"><use href="#treatment-plate"/><text class="number" x="28" y="108" font-size="112">1</text></g>
  <g transform="translate(760 245)" fill="var(--room-2)"><use href="#treatment-plate"/><text class="number" x="22" y="108" font-size="112">2</text></g>
  <g transform="translate(445 447)" fill="var(--room-3)"><use href="#treatment-plate"/><text class="number" x="22" y="108" font-size="112">3</text></g>
  <g transform="translate(760 447)" fill="var(--room-4)"><use href="#treatment-plate"/><text class="number" x="22" y="108" font-size="112">4</text></g>
  <g transform="translate(452 647)" fill="var(--room-5)"><use href="#treatment-plate"/><text class="number" x="22" y="108" font-size="112">5</text></g>
  <g transform="translate(767 647)" fill="var(--room-6)"><use href="#treatment-plate"/><text class="number" x="22" y="108" font-size="112">6</text></g>

  <!-- massage rooms -->
  <rect class="massage-panel" x="415" y="830" width="652" height="183" fill="var(--panel-grey)"/>
  <g transform="translate(455 857)">
    <use href="#massage-plate"/>
    <text class="number" x="38" y="62" font-size="52" text-anchor="middle" fill="var(--massage-blue)">1</text>
  </g>
  <g transform="translate(777 860)">
    <use href="#massage-plate"/>
    <text class="number" x="38" y="62" font-size="52" text-anchor="middle" fill="var(--massage-blue)">2</text>
  </g>
</svg>
</body>
</html>
```